New Real Estate business seek modern cutting edge stationery Design for Letterhead,Presentation fold

We need full stationary designs for new real estate company from Toronto Ontario. We would like a very cool, new, sleek, modern cutting edge design design for email signature, letterhead, envelope and presentation folder.

Let your imagination run wild, looking for a really cool package

Attached is all versions of my logo, the main colours are Red,white and black.

Industry/Entity Type

Real Estate

Requirements
Must have
• Envelope must have a Top secret stamp water marked into the middle
• Presentation folder must have SOLD sign inside
• Follow logo colour seem .
• make all txt editable

```html
<!DOCTYPE html>
<html lang="en">
<head>
<meta charset="utf-8">
<title>Keyhaven Homes Stationery</title>
<link rel="stylesheet" href="https://fonts.googleapis.com/css2?family=Arimo:wght@400;700&family=Open+Sans:wght@400;600&display=swap">
<style>
:root{
  --red:#e8262b;
  --black:#0d0d0d;
  --ink:#3a3a3a;
  --muted:#7a7a7a;
  --paper:#ffffff;
  --backdrop:#ececec;
  --body:"Arimo", Arial, sans-serif;
  --web:"Open Sans", Arial, sans-serif;
}
*{margin:0;padding:0;box-sizing:border-box}
html,body{width:1200px;height:937px;overflow:hidden;background:var(--backdrop);font-family:var(--body);color:var(--ink)}
.canvas{position:relative;width:1200px;height:937px}
.sheet{position:absolute;background:var(--paper);overflow:hidden;box-shadow:0 1px 3px rgba(0,0,0,.12)}

/* brand lockup */
.brand{display:flex;align-items:center;gap:6px}
.brand-mark{background:var(--red);flex:none}
.brand-name{font-family:var(--body);font-weight:400;color:var(--black);line-height:.95;letter-spacing:.3px}
.brand-tag{font-family:var(--body);color:var(--ink);white-space:nowrap}

/* footer band */
.footer{position:absolute;left:0;bottom:0;width:100%}
.footer svg{display:block;width:100%;height:100%}
.footer-url{position:absolute;left:12px;top:50%;transform:translateY(-50%);color:#fff;font-family:var(--web);letter-spacing:.6px}

/* letterhead */
.letterhead{left:185px;top:66px;width:388px;height:546px}
.letterhead .brand{position:absolute;left:36px;top:40px}
.letterhead .brand-mark{width:28px;height:28px}
.letterhead .brand-name{font-size:15px}
.letterhead .brand-tag{position:absolute;left:36px;top:96px;font-size:5px}
.contact{position:absolute;text-align:right;font-size:4.5px;line-height:1.6;color:var(--ink)}
.contact .dot{display:inline-block;width:3px;height:3px;background:var(--red);margin-left:2px;vertical-align:middle}
.letterhead .contact{right:22px;top:24px}
.letter{position:absolute;left:36px;top:138px;width:300px;font-size:4.6px;line-height:1.55;color:var(--ink)}
.letter p{margin-bottom:9px}
.letter .strong{font-weight:700}
.signature{width:30px;height:12px;background:#e3e3e3;margin:4px 0 6px}

/* presentation sheet */
.cover{left:636px;top:40px;width:458px;height:576px}
.cover .brand{position:absolute;left:76px;top:246px;gap:10px}
.cover .brand-mark{width:70px;height:70px}
.cover .brand-name{font-size:34px}
.cover .brand-tag{position:absolute;left:156px;top:322px;font-size:8px}

/* business cards */
.card{width:176px;height:99px;left:45px}
.card-front{top:659px}
.card-back{top:785px}
.card-front .person{position:absolute;left:10px;top:20px;font-size:8px;font-weight:700;color:var(--red)}
.card-front .role{position:absolute;left:10px;top:39px;font-size:5px;color:var(--ink)}
.card-front .rule{position:absolute;left:10px;top:33px;width:60px;height:1px;background:var(--red)}
.card-front .brand{position:absolute;left:82px;top:14px;gap:3px}
.card-front .brand-mark{width:14px;height:14px}
.card-front .brand-name{font-size:8px}
.card-front .contact{right:8px;top:50px;font-size:3.8px}
.card-back .brand{position:absolute;left:40px;top:22px;gap:4px}
.card-back .brand-mark{width:22px;height:22px}
.card-back .brand-name{font-size:12px}
.card-back .brand-tag{position:absolute;left:66px;top:50px;font-size:4px}

/* envelopes */
.envelope{top:672px;width:431px;height:208px}
.envelope-front{left:266px}
.envelope-front .brand{position:absolute;left:12px;top:22px;gap:5px}
.envelope-front .brand-mark{width:36px;height:36px}
.envelope-front .brand-name{font-size:18px}
.envelope-front .brand-tag{position:absolute;left:53px;top:66px;font-size:5px}
.envelope-back{left:737px;width:369px}
.flap{position:absolute;left:0;top:0;width:100%;height:71px}
.flap svg{display:block;width:100%;height:100%}
.flap-url{position:absolute;left:0;right:0;top:30px;text-align:center;color:#fff;font-family:var(--web);font-size:13px;letter-spacing:2px}
</style>
</head>
<body>
<main class="canvas">

  <section class="sheet letterhead" aria-label="Letterhead">
    <div class="brand"><span class="brand-mark"></span><span class="brand-name">Keyhaven<br>Homes</span></div>
    <div class="brand-tag">Your one stop shop for everything Real Estate</div>
    <address class="contact" style="font-style:normal">
      <b>88 Lakeshore Way</b><br>Suite 410<br>416 555 0182<span class="dot"></span><br>hello@keyhavenhomes.com<span class="dot"></span><br>www.keyhavenhomes.com<span class="dot"></span>
    </address>
    <div class="letter">
      <p>July 2, 2012</p>
      <p><span class="strong">Dear Client,</span><br>Harbour Court, 12 Elm St., Toronto</p>
      <p>Thank you for choosing us to guide your next move. Our team brings local market knowledge, honest advice and careful attention to every detail of buying or selling your home. We will keep you informed at every step, from the first viewing to the final signature, so the process stays clear and simple for you and your family.</p>
      <p>Please find enclosed a summary of current listings in your area, along with our recent sales and pricing notes.</p>
      <p style="margin-top:16px">We look forward to meeting you soon to discuss your plans in person. Feel free to call or email our office at any time with questions about financing, timelines, open houses or neighbourhood schools, and we will respond within one business day with the answers you need.</p>
      <p>Best Regards,</p>
      <div class="signature" role="img" aria-label="Handwritten signature"></div>
      <p><span class="strong">Daniel Reyes</span><br>Director<br><br>Harbour Court, 12 Elm St., Toronto</p>
    </div>
    <div class="footer" style="height:18px">
      <svg viewBox="0 0 388 18" preserveAspectRatio="none"><path d="M0 0H120Q132 0 140 18H0Z" fill="#0d0d0d"/><rect x="138" y="9" width="250" height="9" fill="#e8262b"/></svg>
      <span class="footer-url" style="font-size:6px">www.keyhavenhomes.com</span>
    </div>
  </section>

  <section class="sheet cover" aria-label="Presentation sheet">
    <div class="brand"><span class="brand-mark"></span><span class="brand-name">Keyhaven<br>Homes</span></div>
    <div class="brand-tag">Your one stop shop for everything Real Estate</div>
    <div class="footer" style="height:20px">
      <svg viewBox="0 0 458 20" preserveAspectRatio="none"><path d="M0 0H172Q184 0 192 20H0Z" fill="#0d0d0d"/><rect x="190" y="9" width="268" height="11" fill="#e8262b"/></svg>
      <span class="footer-url" style="font-size:7.5px">www.keyhavenhomes.com</span>
    </div>
  </section>

  <section class="sheet card card-front" aria-label="Business card front">
    <div class="person">Marcus Lee</div>
    <div class="rule"></div>
    <div class="role">CEO</div>
    <div class="brand"><span class="brand-mark"></span><span class="brand-name">Keyhaven<br>Homes</span></div>
    <address class="contact" style="font-style:normal">88 Lakeshore Way<br>Suite 410<br>416 555 0182<span class="dot"></span><br>hello@keyhavenhomes.com<span class="dot"></span><br>www.keyhavenhomes.com<span class="dot"></span></address>
    <div class="footer" style="height:9px">
      <svg viewBox="0 0 176 9" preserveAspectRatio="none"><path d="M0 0H54Q60 0 64 9H0Z" fill="#0d0d0d"/><rect x="63" y="5" width="113" height="4" fill="#e8262b"/></svg>
      <span class="footer-url" style="font-size:3.6px;left:5px">www.keyhavenhomes.com</span>
    </div>
  </section>

  <section class="sheet card card-back" aria-label="Business card back">
    <div class="brand"><span class="brand-mark"></span><span class="brand-name">Keyhaven<br>Homes</span></div>
    <div class="brand-tag">Your one stop shop for everything Real Estate</div>
    <div class="footer" style="height:9px">
      <svg viewBox="0 0 176 9" preserveAspectRatio="none"><rect x="0" y="5" width="100" height="4" fill="#e8262b"/><path d="M176 0H112Q106 0 102 9H176Z" fill="#0d0d0d"/></svg>
      <span class="footer-url" style="font-size:3.6px;left:auto;right:5px">www.keyhavenhomes.com</span>
    </div>
  </section>

  <section class="sheet envelope envelope-front" aria-label="Envelope front">
    <div class="brand"><span class="brand-mark"></span><span class="brand-name">Keyhaven<br>Homes</span></div>
    <div class="brand-tag">Your one stop shop for everything Real Estate</div>
    <div class="footer" style="height:22px">
      <svg viewBox="0 0 431 22" preserveAspectRatio="none"><path d="M0 0H160Q172 0 180 22H0Z" fill="#0d0d0d"/><rect x="178" y="11" width="253" height="11" fill="#e8262b"/></svg>
      <span class="footer-url" style="font-size:9px">www.keyhavenhomes.com</span>
    </div>
  </section>

  <section class="sheet envelope envelope-back" aria-label="Envelope back">
    <div class="flap">
      <svg viewBox="0 0 369 71" preserveAspectRatio="none"><path d="M0 0H369V30Q369 50 345 54Q300 62 260 64H60Q28 62 14 56Q0 50 0 36Z" fill="#0d0d0d"/></svg>
      <span class="flap-url">www.<b>keyhavenhomes</b>.com</span>
    </div>
  </section>

</main>
</body>
</html>
```